Designing a website for Korvale Pest Solutions PTY LTD

Pest control company looking for someone to build an informative website containing services we offer and an online inquiry form.
Commercial premises - Specialising in - Rodent control, stored product pest control, flying insect control, ant, spider and insect control, Termite inspections and treatments. Termite management systems on a commercial scale.
Facilities we service
Commercial - shopping centres, transport facilities, restaurants, pubs, clubs, bars food manufacturing facilities.
Residential - Houses specialising in - Rodent, Ant, Spider, Cockroach and Termite control. Termite inspections, Pre - purchase inspections, Termite treatments, Termite management systems.
Target Market(s)
Mainly commercial and industrial clients and Residential clients.
Industry/Entity Type
Pest Control
Number of Pages Required
1 page
Look and feel
Each slider illustrates characteristics of the customer's brand and the style your logo design should communicate.

```html
<!DOCTYPE html>
<html lang="en">
<head>
<meta charset="utf-8">
<title>Korvale Pest Solutions PTY LTD</title>
<link rel="stylesheet" href="https://fonts.googleapis.com/css2?family=Open+Sans:wght@400;600;700&family=Ubuntu:wght@400;500;700&display=swap">
<style>
  :root {
    --dark: #2e2e2e;
    --dark-deep: #262626;
    --hero-light: #f2f2f2;
    --hero-mid: #d9d9d9;
    --green: #5e9a2a;
    --green-bright: #8cc63f;
    --green-pale: #b6e07a;
    --ink: #2a2a2a;
    --muted: #6a6a6a;
    --nav: #cfcfcf;
    --rule: #8a8a8a;
    --art-grey: #a9a9a9;
  }
  * { box-sizing: border-box; margin: 0; padding: 0; }
  html, body { width: 1200px; height: 788px; overflow: hidden; background: var(--dark); }
  .page { position: relative; width: 1200px; height: 788px; background: var(--dark); font-family: "Open Sans", sans-serif; overflow: hidden; }

  .site-header { position: absolute; top: 0; left: 0; right: 0; height: 64px; background: var(--dark-deep); display: flex; justify-content: flex-end; align-items: center; padding-right: 70px; gap: 64px; z-index: 3; }
  .site-header a { color: var(--nav); text-decoration: none; font-family: "Ubuntu", sans-serif; font-size: 17px; letter-spacing: .5px; }
  .site-header a:last-child { color: #fff; }

  .hero { position: absolute; top: 64px; left: 0; right: 0; height: 400px; background: linear-gradient(100deg, var(--hero-light) 0%, #e8e8e8 45%, var(--hero-mid) 100%); }
  .hero-copy { position: absolute; top: 40px; left: 70px; width: 520px; z-index: 2; }
  .hero-title { font-family: "Ubuntu", sans-serif; font-weight: 700; font-size: 38px; line-height: 1.15; color: var(--ink); }
  .hero-lead { margin-top: 18px; font-weight: 700; font-size: 17px; line-height: 1.35; color: var(--green); }
  .hero-note { margin-top: 10px; font-size: 14px; color: var(--muted); }
  .hero-note strong { color: var(--ink); }
  .btn-contact { display: inline-flex; align-items: center; gap: 12px; margin-top: 22px; padding: 12px 26px 12px 14px; background: linear-gradient(180deg, var(--green-pale), var(--green-bright)); color: #3d5e1b; font-size: 12px; font-weight: 700; letter-spacing: 1px; text-transform: uppercase; text-decoration: none; border-radius: 2px; }
  .btn-contact .dot { width: 20px; height: 20px; border-radius: 50%; background: var(--green); }

  .hero-art { position: absolute; top: 20px; left: 620px; width: 500px; height: 360px; border-radius: 6px; background: radial-gradient(ellipse at 55% 50%, var(--art-grey) 0%, #c4c4c4 45%, #d6dccd 75%, #dfe5d6 100%); }

  .services { position: absolute; top: 464px; left: 0; right: 0; bottom: 0; }
  .services-title { position: absolute; top: 50px; left: 70px; color: #f0f0f0; font-family: "Ubuntu", sans-serif; font-weight: 400; font-size: 28px; letter-spacing: 2px; text-transform: uppercase; }
  .services-rule { position: absolute; top: 95px; left: 70px; width: 1060px; height: 1px; background: var(--rule); }
  .service-icon { position: absolute; top: 122px; left: 70px; width: 30px; height: 30px; border: 3px solid var(--green-bright); }
  .service-icon::after { content: ""; position: absolute; left: 9px; top: 5px; width: 6px; height: 14px; background: var(--green-bright); }
  .service-photo { position: absolute; top: 130px; left: 300px; width: 540px; height: 200px; background: linear-gradient(160deg, #e8e4df 0%, #b48a74 45%, #8a6a5a 70%, #d8d4cf 100%); }
</style>
</head>
<body>
<div class="page">
  <nav class="site-header">
    <a href="#commercial">Comercial</a>
    <a href="#residential">Residencial</a>
    <a href="#contact">Conatct</a>
  </nav>

  <section class="hero">
    <div class="hero-copy">
      <h1 class="hero-title">The ultimate commercial pest control solution.</h1>
      <p class="hero-lead">We are experts in rodent control, stored product pest control, flying insect control, ant, spider and insect control, termite inspections and treatments.</p>
      <p class="hero-note">Termite management systems on a <strong>commercial scale.</strong></p>
      <a class="btn-contact" href="#contact"><span class="dot"></span>Contact now</a>
    </div>
    <div class="hero-art" role="img" aria-label="Green and black curved emblem framing silhouettes of a rat, flies, a cockroach, a spider and ants"></div>
  </section>

  <section class="services">
    <h2 class="services-title">Service Facilities</h2>
    <div class="services-rule"></div>
    <div class="service-icon"></div>
    <div class="service-photo" role="img" aria-label="Aerial view of a shopping centre food court"></div>
  </section>
</div>
</body>
</html>
```